Business Card Design

I need a business card for my rental business. The business is named:
Hire a Vorlatrike Brenmoor
www.hireavorlatrikebrenmoor.example
(555) 014-2937
This will be a business card that I will leave at other businesses as advertisement so it needs to have the name, website, and phone number.
Please feel free to be creative. This is a new business so I have no designs.
Thank you very much for your time and I look forward to receiving your designs
Target Market(s)
Local rental customers
Industry/Entity Type
Business
Contact Information for Business Card
Please check out my website:
Other font styles liked:
- anything creative
Colors
Designer to choose colors to be used in the design.
Requirements
Must have
- Business name, phone, website. Rentals available hourly or daily. Book online

```html
<!DOCTYPE html>
<html lang="en">
<head>
<meta charset="utf-8">
<title>Hire a Vorlatrike Brenmoor – Business Card</title>
<link rel="stylesheet" href="https://fonts.googleapis.com/css2?family=Oswald:wght@400;500&family=Raleway:wght@300&display=swap">
<style>
  :root {
    --brand-red: #dc1a35;
    --brand-red-deep: #c8102e;
    --card-white: #f2f2f2;
    --ink: #1c1c1c;
    --backdrop: #e9e9e9;
  }
  * { box-sizing: border-box; margin: 0; padding: 0; }
  html, body { width: 1200px; height: 1152px; overflow: hidden; }
  body {
    background: var(--backdrop);
    display: flex;
    flex-direction: column;
    align-items: center;
    justify-content: center;
    gap: 80px;
    font-family: "Oswald", sans-serif;
  }
  .card {
    position: relative;
    width: 700px;
    height: 400px;
    overflow: hidden;
    box-shadow: 0 6px 18px rgba(0,0,0,0.12);
  }

  /* Front */
  .card-front { background: var(--card-white); }
  .front-band {
    position: absolute;
    left: 0; right: 0; top: 110px;
    height: 120px;
    background: var(--brand-red);
    display: flex;
    align-items: center;
    justify-content: center;
  }
  .front-name {
    color: #fff;
    font-weight: 500;
    font-size: 54px;
    letter-spacing: 0.5px;
    text-transform: uppercase;
    transform: scaleY(1.15);
  }
  .front-web {
    position: absolute;
    left: 0; right: 0; top: 300px;
    text-align: center;
    color: var(--ink);
    font-size: 20px;
    text-transform: uppercase;
  }

  /* Back */
  .card-back { background: var(--brand-red); color: #fff; }
  .back-texture {
    position: absolute; inset: 0;
    background: linear-gradient(135deg, var(--brand-red) 0%, var(--brand-red-deep) 100%);
  }
  .back-band {
    position: absolute;
    left: 0; right: 0; top: 38px;
    height: 96px;
    background: var(--card-white);
    display: flex;
    align-items: center;
    justify-content: center;
  }
  .back-name {
    color: var(--brand-red);
    font-weight: 500;
    font-size: 48px;
    text-transform: uppercase;
    transform: scaleY(1.15);
  }
  .back-details {
    position: absolute;
    left: 0; right: 0; top: 160px;
    text-align: center;
    font-size: 19px;
    line-height: 1.35;
    text-transform: uppercase;
  }
  .availability {
    position: absolute;
    left: 0; right: 0; top: 268px;
    display: flex;
    align-items: center;
    justify-content: center;
    gap: 18px;
    font-family: "Raleway", sans-serif;
    font-weight: 300;
    font-size: 23px;
    letter-spacing: 1px;
    text-transform: uppercase;
  }
  .availability .rule { width: 70px; height: 1px; background: rgba(255,255,255,0.8); }
  .booking {
    position: absolute;
    left: 0; right: 0; top: 322px;
    text-align: center;
    font-size: 19px;
    text-transform: uppercase;
    word-spacing: 2px;
  }
  .booking .gap { display: inline-block; width: 18px; }
</style>
</head>
<body>
  <section class="card card-front">
    <div class="front-band"><h1 class="front-name">Hire a Vorlatrike Brenmoor</h1></div>
    <p class="front-web">www.hireavorlatrikebrenmoor.example</p>
  </section>

  <section class="card card-back">
    <div class="back-texture" role="img" aria-label="Subtle red diamond pattern background"></div>
    <div class="back-band"><h2 class="back-name">Hire a Vorlatrike Brenmoor</h2></div>
    <address class="back-details" style="font-style:normal">
      (555) 014-2937<br>
      FM-904, Brenmoor,<br>
      Kestral 00421, United States
    </address>
    <p class="availability"><span class="rule"></span>Rentals available hourly or daily<span class="rule"></span></p>
    <p class="booking">Book online on<span class="gap"></span>www.hireavorlatrikebrenmoor.example</p>
  </section>
</body>
</html>
```